business card design for luxurious real estate brand

using the attached logo, i am looking for a 2-sided business card design. the back should be the gold logo on black background. the front needs to include: gold logo, name, phone, email, and website

Industry/Entity Type

real estate

Contact Information for Business Card

logo, name, email, phone, website

Font styles to use
Sans Serif

```html
<!DOCTYPE html>
<html lang="en">
<head>
<meta charset="utf-8">
<title>Casa Verano – Business Card</title>
<link rel="stylesheet" href="https://fonts.googleapis.com/css2?family=Arimo:wght@400;700&display=swap">
<style>
  :root {
    --bg: #d9d9d9;
    --card: #1c1c1c;
    --gold: #f5c400;
    --ink-light: #f2f2f2;
    --divider: #3a3a3a;
  }
  * { box-sizing: border-box; margin: 0; padding: 0; }
  html, body {
    width: 1200px; height: 792px; overflow: hidden;
    background: var(--bg);
    font-family: "Arimo", Arial, sans-serif;
  }
  .canvas {
    width: 1200px; height: 792px;
    display: flex; align-items: center; justify-content: center; gap: 40px;
  }
  .card {
    position: relative;
    width: 560px; height: 320px;
    background: var(--card);
    border-radius: 22px;
    overflow: hidden;
  }
  .card--front { border-bottom: 9px solid var(--gold); }
  .card--back { border-bottom: 3px solid var(--gold); }

  .brand {
    display: flex; align-items: center; gap: 12px;
    color: var(--gold);
    font-weight: 700;
    letter-spacing: 0.18em;
    text-transform: uppercase;
    white-space: nowrap;
  }
  .brand-mark { background: var(--gold); flex: none; }

  .front-brand {
    position: absolute; left: 0; top: 0; bottom: 0; width: 290px;
    display: flex; align-items: center; justify-content: center;
  }
  .front-brand .brand { font-size: 22px; }
  .front-brand .brand-mark { width: 14px; height: 14px; }

  .divider {
    position: absolute; left: 290px; top: 40px; bottom: 40px; width: 1px;
    background: linear-gradient(to bottom, transparent, var(--divider) 20%, var(--divider) 80%, transparent);
  }

  .contact {
    position: absolute; left: 318px; top: 62px; right: 20px;
    color: var(--ink-light); font-size: 13px; line-height: 1.35;
  }
  .contact-name { color: var(--gold); font-weight: 700; font-size: 21px; line-height: 1.1; }
  .contact-title { font-size: 13px; margin-bottom: 16px; }
  .contact-address { margin-bottom: 16px; }
  .contact-list { list-style: none; }
  .contact-list li { display: flex; align-items: center; gap: 8px; margin-bottom: 3px; }
  .contact-icon { width: 12px; height: 12px; flex: none; }

  .back-brand {
    position: absolute; inset: 0;
    display: flex; align-items: center; justify-content: center;
  }
  .back-brand .brand { font-size: 34px; gap: 16px; }
  .back-brand .brand-mark { width: 20px; height: 20px; }
</style>
</head>
<body>
<main class="canvas">

  <section class="card card--front" aria-label="Card front">
    <div class="front-brand">
      <div class="brand"><span class="brand-mark"></span>Casa Verano</div>
    </div>
    <div class="divider"></div>
    <div class="contact">
      <p class="contact-name">Daniel Morrow</p>
      <p class="contact-title">Managing Director</p>
      <p class="contact-address">412 Willow Crest Road<br>Fairview, Oregon 97024</p>
      <ul class="contact-list">
        <li>
          <svg class="contact-icon" viewBox="0 0 12 12" aria-hidden="true"><path fill="#f5c400" d="M2.5 1 4.5 1 5.3 3.6 4 4.6C4.7 6 6 7.3 7.4 8l1-1.3L11 7.5v2C11 10.3 10.3 11 9.5 11 5 11 1 7 1 2.5 1 1.7 1.7 1 2.5 1Z"/></svg>
          555-281-0947
        </li>
        <li>
          <svg class="contact-icon" viewBox="0 0 12 12" aria-hidden="true"><rect x="0.5" y="2" width="11" height="8" rx="1" fill="#f5c400"/><path d="M1 2.6 6 6.5 11 2.6" fill="none" stroke="#1c1c1c" stroke-width="1"/></svg>
          hello@casaverano.com
        </li>
        <li>
          <svg class="contact-icon" viewBox="0 0 12 12" aria-hidden="true"><circle cx="6" cy="6" r="5.5" fill="#f5c400"/><path d="M0.5 6h11M6 0.5c-2.4 3-2.4 8 0 11M6 0.5c2.4 3 2.4 8 0 11" fill="none" stroke="#1c1c1c" stroke-width="0.8"/></svg>
          www.casaverano.com
        </li>
      </ul>
    </div>
  </section>

  <section class="card card--back" aria-label="Card back">
    <div class="back-brand">
      <div class="brand"><span class="brand-mark"></span>Casa Verano</div>
    </div>
  </section>

</main>
</body>
</html>
```